Business Card Design for Small Electrical Contractor

I need to update my business card into something a little more modern. We are a small electrical contracting company. We service domestic and commercial places around Sydney. We have 2 logo designs at the moment. I have uploaded both and 2 different sizes to work with.

Industry/Entity Type

Business

Contact Information for Business Card

Leo Hartigan
8/21-23 Birch Rd, Kelsworth 2087
t - (02) 9381 4720
m - 0427 815 903
E - info@hartiganelx.com.au
W - hartiganelx.com.au
ABN: 42 907 551 316

Font styles to use
Sans Serif

Requirements
Must have
• I would also like to see the below fit on somewhere aswell
• - Licensed Electrician
• - Level 2 (Cat 1 & 4)
• - Domestic
• - Commercial
• - Repairs and Installations
• - Data
Nice to have
• Try and keep similar colours as logo
Should not have
• No lightning bolts or light globes. Smart and professional please.

```html
<!DOCTYPE html>
<html lang="en">
<head>
<meta charset="utf-8">
<title>Hartigan Electrical – Business Card</title>
<link href="https://fonts.googleapis.com/css2?family=Open+Sans:wght@400;600;700&display=swap" rel="stylesheet">
<style>
  :root {
    --ink: #0f2a22;
    --orange: #f47c12;
    --paper: #ffffff;
    --paper-shade: #eef0ef;
    --rule: #6d6f6e;
  }
  * { margin: 0; padding: 0; box-sizing: border-box; }
  html, body { width: 1200px; height: 741px; overflow: hidden; }
  body { font-family: "Open Sans", Arial, sans-serif; color: var(--ink); }
  .card {
    position: relative;
    width: 1200px;
    height: 741px;
    overflow: hidden;
    background: linear-gradient(135deg, var(--paper) 0%, #f7f8f8 40%, var(--paper-shade) 75%, #f8f9f9 100%);
  }
  .card__texture {
    position: absolute;
    inset: 0;
    background: linear-gradient(160deg, rgba(255,255,255,0) 30%, rgba(230,233,232,0.5) 60%, rgba(255,255,255,0) 85%);
  }
  .brand {
    position: absolute;
    left: 140px;
    top: 221px;
    width: 304px;
    height: 304px;
    border-radius: 50%;
    background: var(--paper);
    border: 6px solid var(--ink);
    display: flex;
    align-items: center;
    justify-content: center;
    text-align: center;
  }
  .brand__name {
    font-weight: 700;
    font-size: 30px;
    line-height: 1.2;
    color: var(--ink);
  }
  .divider {
    position: absolute;
    left: 544px;
    top: 144px;
    width: 1px;
    height: 474px;
    background: var(--rule);
  }
  .details {
    position: absolute;
    left: 644px;
    top: 176px;
  }
  .details__name {
    font-weight: 700;
    font-size: 37px;
    letter-spacing: 1px;
    text-transform: uppercase;
    line-height: 1;
  }
  .details__address {
    margin-top: 20px;
    font-size: 21px;
    letter-spacing: 0.3px;
  }
  .contacts { list-style: none; margin-top: 30px; }
  .contact {
    display: flex;
    align-items: center;
    height: 52px;
    margin-bottom: 13px;
    font-size: 19.5px;
    letter-spacing: 0.2px;
  }
  .contact svg { width: 52px; height: 52px; flex: none; margin-right: 26px; }
  .details__abn { margin-top: 24px; margin-left: 2px; font-size: 21.5px; letter-spacing: 0.2px; }
  .services {
    position: absolute;
    left: 0;
    right: 0;
    top: 660px;
    display: flex;
    justify-content: center;
    list-style: none;
    font-size: 16px;
    font-weight: 600;
    letter-spacing: 0.4px;
    color: var(--ink);
  }
  .services li + li::before {
    content: "";
    display: inline-block;
    width: 6px;
    height: 6px;
    border-radius: 50%;
    background: var(--orange);
    margin: 0 14px 3px;
    vertical-align: middle;
  }
</style>
</head>
<body>
<div class="card">
  <div class="card__texture" role="img" aria-label="Soft faceted light-grey background"></div>

  <div class="brand">
    <span class="brand__name">Hartigan<br>Electrical</span>
  </div>

  <div class="divider"></div>

  <div class="details">
    <h1 class="details__name">Leo Hartigan</h1>
    <p class="details__address">8/21-23 Birch Rd, Kelsworth 2087</p>
    <ul class="contacts">
      <li class="contact">
        <svg viewBox="0 0 52 52" aria-hidden="true">
          <circle cx="26" cy="26" r="24" fill="var(--paper)" stroke="var(--ink)" stroke-width="3"/>
          <circle cx="26" cy="26" r="20" fill="none" stroke="var(--orange)" stroke-width="3"/>
          <path d="M19 16 l4 -1 l3 6 l-3 2 q2 5 6 7 l2 -3 l6 3 l-1 4 q-4 2 -9 -1 q-7 -5 -9 -11 q-1 -4 1 -6z" fill="none" stroke="var(--ink)" stroke-width="1.8" stroke-linejoin="round"/>
          <path d="M30 16 q5 1 6 6 M30 20 q2 0 2 2" fill="none" stroke="var(--ink)" stroke-width="1.6" stroke-linecap="round"/>
        </svg>
        <span>(02) 9381 4720</span>
      </li>
      <li class="contact">
        <svg viewBox="0 0 52 52" aria-hidden="true">
          <circle cx="26" cy="26" r="24" fill="var(--paper)" stroke="var(--ink)" stroke-width="3"/>
          <circle cx="26" cy="26" r="20" fill="none" stroke="var(--orange)" stroke-width="3"/>
          <rect x="19" y="13" width="14" height="26" rx="2.5" fill="none" stroke="var(--ink)" stroke-width="2"/>
          <line x1="19" y1="17" x2="33" y2="17" stroke="var(--ink)" stroke-width="1.5"/>
          <line x1="19" y1="34" x2="33" y2="34" stroke="var(--ink)" stroke-width="1.5"/>
          <circle cx="26" cy="36.5" r="1" fill="var(--ink)"/>
        </svg>
        <span>&nbsp;0427 815 903</span>
      </li>
      <li class="contact">
        <svg viewBox="0 0 52 52" aria-hidden="true">
          <circle cx="26" cy="26" r="24" fill="var(--paper)" stroke="var(--ink)" stroke-width="3"/>
          <circle cx="26" cy="26" r="20" fill="none" stroke="var(--orange)" stroke-width="3"/>
          <circle cx="26" cy="26" r="13" fill="var(--ink)"/>
          <rect x="11" y="22" width="30" height="8" fill="var(--paper)"/>
          <text x="26" y="29" text-anchor="middle" font-family="Open Sans, Arial, sans-serif" font-weight="700" font-size="7.5" fill="var(--ink)">www</text>
        </svg>
        <span>info@hartiganelx.com.au</span>
      </li>
      <li class="contact">
        <svg viewBox="0 0 52 52" aria-hidden="true">
          <circle cx="26" cy="26" r="24" fill="var(--paper)" stroke="var(--ink)" stroke-width="3"/>
          <circle cx="26" cy="26" r="20" fill="none" stroke="var(--orange)" stroke-width="3"/>
          <rect x="15" y="19" width="22" height="15" rx="2" fill="var(--ink)"/>
          <path d="M15.5 20 L26 28 L36.5 20" fill="none" stroke="var(--paper)" stroke-width="1.8"/>
        </svg>
        <span>hartiganelx.com.au</span>
      </li>
    </ul>
    <p class="details__abn">ABN: 42 907 551 316</p>
  </div>

  <ul class="services">
    <li>Licensed Electrician</li>
    <li>Level 2 (Cat 1 &amp; 4)</li>
    <li>Domestic</li>
    <li>Commercial</li>
    <li>Repairs and Installations</li>
    <li>Data</li>
  </ul>
</div>
</body>
</html>
```